Market Research firm needs updated business cards with new logo

We need the logo to be included somewhere on the card (attached). We would also like the phrases "Independent, Objective, Comprehensive" and "Research You Can Trust" somewhere on the card. Front or back. Our colors are hex codes 6075a7, e48d25 and 5a5b5b. Though you are certainly not limited to those shades, whatever you produce should coordinate with them. I have also attached our favicon. Feel free to use it in your design, but please do not use it to replace the full logo.

Contact Information for Business Card

see project description

Font styles to use
Other font styles liked:
• Open Sans

Requirements
Must have
• the logo
• We use Open Sans font

```html
<!DOCTYPE html>
<html lang="en">
<head>
<meta charset="utf-8">
<title>Veridan Research – Business Card</title>
<link rel="stylesheet" href="https://fonts.googleapis.com/css2?family=Questrial&display=swap">
<style>
  :root {
    --orange: #ef8426;
    --slate: #6b7886;
    --ink: #222325;
    --paper: #ffffff;
    --backdrop: #2f3033;
    --rule: #7d8690;
  }
  * { margin: 0; padding: 0; box-sizing: border-box; }
  html, body {
    width: 1082px; height: 1200px; overflow: hidden;
    background: var(--backdrop);
    font-family: "Questrial", sans-serif;
  }
  .card {
    position: absolute; left: 172px;
    width: 739px; height: 410px;
    border-radius: 0 0 32px 32px;
    overflow: hidden;
  }
  .card-back { top: 154px; background: var(--slate); }
  .card-front { top: 636px; background: var(--paper); }

  .back-name {
    position: absolute; left: 0; width: 100%; top: 160px;
    text-align: center; color: var(--orange); font-size: 56px; line-height: 1;
  }
  .back-motto {
    position: absolute; left: 0; width: 100%; top: 236px;
    text-align: center; color: var(--paper);
    font-size: 18px; letter-spacing: 2px; line-height: 1;
  }

  .front-art { position: absolute; inset: 0; }
  .wordmark {
    position: absolute; right: 211px; top: 42px;
    color: var(--orange); font-size: 56px; line-height: 1; white-space: nowrap;
  }
  .person-name {
    position: absolute; right: 211px; top: 124px;
    color: var(--ink); font-size: 32px; line-height: 1;
  }
  .person-title {
    position: absolute; right: 211px; top: 158px;
    color: var(--ink); font-size: 20px; line-height: 1;
  }
  .divider {
    position: absolute; left: 561px; top: 36px;
    width: 2px; height: 150px; background: var(--rule);
  }
  .tagline {
    position: absolute; left: 594px; top: 62px;
    color: var(--orange); font-size: 25px; line-height: 32px;
  }
  .contact {
    position: absolute; color: var(--paper);
    font-size: 22px; line-height: 28px; white-space: nowrap;
  }
  .contact-phones { left: 34px; top: 216px; }
  .contact-web { left: 436px; top: 244px; }
  .address {
    position: absolute; left: 0; width: 100%; top: 362px;
    text-align: center; color: var(--paper); font-size: 21px;
  }
</style>
</head>
<body>

<section class="card card-back">
  <div class="back-name">Veridan</div>
  <div class="back-motto">INDEPENDENT • OBJECTIVE • COMPREHENSIVE</div>
</section>

<section class="card card-front">
  <svg class="front-art" width="739" height="410" viewBox="0 0 739 410">
    <path d="M0,178 C180,160 340,212 480,222 C600,230 690,205 739,168 L739,336 L0,336 Z" fill="var(--orange)"/>
    <rect x="0" y="340" width="739" height="70" fill="var(--slate)"/>
  </svg>

  <div class="wordmark">Veridan Research</div>
  <div class="person-name">Jana Holt</div>
  <div class="person-title">CEO</div>
  <div class="divider"></div>
  <div class="tagline">Research<br>You Can<br>Trust</div>

  <div class="contact contact-phones">
    Office: 555 000 5555 ext. 55<br>
    Fax: 555 000 5555<br>
    Cell: 555 000 5555<br>
    Toll Free: 555 000 5555
  </div>
  <div class="contact contact-web">
    jholt@veridanresearch.com<br>
    www.veridanresearch.com
  </div>

  <div class="address">12 Elm Street P.O. Box 555 Fairview, KS 5555</div>
</section>

</body>
</html>
```